Fish guide business card

Buisiness card

Target Market(s)

Visitors to Campbell River Bc wanting to catch fish in the ocean and have a memorable adventure fun filled day

Industry/Entity Type

Tourism

Contact Information for Business Card

Phone number 250 318 two cards Ray 250 318 7262 other card Lou 250 6093714 both have email info@lwgullrocktours.com and website www.lwgullrocktours.com

Requirements
Must have
• Email, website , name , phone , logo , Campbell River BC
Nice to have
• Uploaded pictures have boat and man with fish picture

```html
<!DOCTYPE html>
<html lang="en">
<head>
<meta charset="utf-8">
<title>LW Gull Rock Tours – Business Card</title>
<link href="https://fonts.googleapis.com/css2?family=Poppins:wght@400;600;700&display=swap" rel="stylesheet">
<style>
  :root {
    --navy: #262262;
    --white: #ffffff;
    --backdrop: #d3d4d6;
    --ink: #2b2b2b;
  }
  * { margin: 0; padding: 0; box-sizing: border-box; }
  html, body { width: 900px; height: 1200px; overflow: hidden; }
  body {
    background: var(--backdrop);
    font-family: "Poppins", Arial, sans-serif;
    position: relative;
  }
  .card {
    position: absolute;
    left: 120px;
    width: 660px;
    height: 380px;
    overflow: hidden;
  }
  .card-front { top: 202px; background: var(--navy); }
  .card-back { top: 619px; background: var(--white); }

  .brand-seal {
    position: absolute;
    border-radius: 50%;
    display: flex;
    align-items: center;
    justify-content: center;
    text-align: center;
    font-weight: 700;
    line-height: 1.2;
  }
  .card-front .brand-seal {
    left: 195px; top: 55px;
    width: 270px; height: 270px;
    border: 8px solid var(--white);
    color: var(--white);
    font-size: 32px;
  }
  .back-band {
    position: absolute;
    left: 0; top: 0;
    width: 172px; height: 100%;
    background: var(--navy);
  }
  .card-back .brand-seal {
    left: 70px; top: 88px;
    width: 202px; height: 202px;
    background: var(--white);
    color: var(--navy);
    font-size: 21px;
    box-shadow: inset 0 0 0 10px var(--white), inset 0 0 0 14px var(--navy);
  }
  .divider {
    position: absolute;
    left: 296px; top: 97px;
    width: 2px; height: 200px;
    background: var(--navy);
  }
  .contact-block {
    position: absolute;
    left: 329px; top: 104px;
  }
  .person-name {
    color: var(--navy);
    font-weight: 700;
    font-size: 29px;
    line-height: 1.1;
    letter-spacing: 0.3px;
  }
  .person-title {
    color: var(--ink);
    font-size: 15px;
    line-height: 1.3;
    padding-bottom: 6px;
    border-bottom: 1.5px solid var(--navy);
    width: 150px;
    letter-spacing: 0.3px;
  }
  .contact-list { list-style: none; margin-top: 10px; }
  .contact-list li {
    display: flex;
    align-items: center;
    height: 25px;
    font-size: 15.5px;
    color: var(--ink);
    letter-spacing: 0.4px;
    white-space: nowrap;
  }
  .contact-list li.phone { letter-spacing: 2.4px; }
  .contact-list svg { width: 15px; height: 15px; margin-right: 6px; fill: var(--navy); flex: none; }
</style>
</head>
<body>

  <section class="card card-front">
    <div class="brand-seal">LW Gull Rock<br>Tours</div>
  </section>

  <section class="card card-back">
    <div class="back-band"></div>
    <div class="brand-seal">LW Gull Rock<br>Tours</div>
    <div class="divider"></div>
    <div class="contact-block">
      <h1 class="person-name">RAY MORROW</h1>
      <p class="person-title">Executive Director</p>
      <ul class="contact-list">
        <li class="phone">
          <svg viewBox="0 0 24 24"><path d="M6.6 10.8a15.1 15.1 0 0 0 6.6 6.6l2.2-2.2c.3-.3.7-.4 1-.2 1.1.4 2.3.6 3.6.6.6 0 1 .4 1 1V20c0 .6-.4 1-1 1A17 17 0 0 1 3 4c0-.6.4-1 1-1h3.5c.6 0 1 .4 1 1 0 1.3.2 2.5.6 3.6.1.3 0 .7-.2 1z"/></svg>
          250 318 7262
        </li>
        <li class="phone">
          <svg viewBox="0 0 24 24"><path d="M6.6 10.8a15.1 15.1 0 0 0 6.6 6.6l2.2-2.2c.3-.3.7-.4 1-.2 1.1.4 2.3.6 3.6.6.6 0 1 .4 1 1V20c0 .6-.4 1-1 1A17 17 0 0 1 3 4c0-.6.4-1 1-1h3.5c.6 0 1 .4 1 1 0 1.3.2 2.5.6 3.6.1.3 0 .7-.2 1z"/></svg>
          250 609 3714
        </li>
        <li>
          <svg viewBox="0 0 24 24"><path d="M2 5h20v14H2V5zm2 2v.4l8 5.3 8-5.3V7H4zm16 2.8-8 5.3-8-5.3V17h16V9.8z"/></svg>
          info@lwgullrocktours.com
        </li>
        <li>
          <svg viewBox="0 0 24 24"><path d="M12 2a10 10 0 1 0 0 20 10 10 0 0 0 0-20zm6.9 6h-3a15.7 15.7 0 0 0-1.4-3.6A8 8 0 0 1 18.9 8zM12 4c.8 1.2 1.5 2.5 1.9 4h-3.8c.4-1.5 1.1-2.8 1.9-4zM4.3 14a8.2 8.2 0 0 1 0-4h3.4a16.5 16.5 0 0 0 0 4H4.3zm.8 2h3a15.7 15.7 0 0 0 1.4 3.6A8 8 0 0 1 5.1 16zm3-8h-3a8 8 0 0 1 4.4-3.6C8.9 5.5 8.4 6.7 8.1 8zM12 20c-.8-1.2-1.5-2.5-1.9-4h3.8c-.4 1.5-1.1 2.8-1.9 4zm2.3-6H9.7a14.7 14.7 0 0 1 0-4h4.6a14.7 14.7 0 0 1 0 4zm.2 5.6c.6-1.1 1.1-2.3 1.4-3.6h3a8 8 0 0 1-4.4 3.6zm1.8-5.6a16.5 16.5 0 0 0 0-4h3.4a8.2 8.2 0 0 1 0 4h-3.4z"/></svg>
          www.lwgullrocktours.com
        </li>
        <li>
          <svg viewBox="0 0 24 24"><path d="M12 2a7 7 0 0 0-7 7c0 5.2 7 13 7 13s7-7.8 7-13a7 7 0 0 0-7-7zm0 9.5a2.5 2.5 0 1 1 0-5 2.5 2.5 0 0 1 0 5z"/></svg>
          Campbell River BC
        </li>
      </ul>
    </div>
  </section>

</body>
</html>
```